Alcohol Marketing website

Home page and information page design, details as follows

CLIENT PURPOSE
Increase online visibility and create good contacts to increase business.

SERVICES
Drinks Marketing Consultancy
Brand Representation
Spirit Brand Sales & Marketing
Brand Development
Brand Distribution
Brand Launch & Introductions

COMPETITION
hazelpour.co.uk -
quintaloft.co.uk -

WEBSITE(S) CLIENT LIKES
Small competitors I admire:
http://www.hazelpour.co.uk/main.htm
http://www.quintaloft.com
http://www.morvatide.co.uk/spiritsliqueursbybrand.php
http://www.kelbrowhouse.com/page1.html
http://www.quorrifenwave.co.uk/index.asp

Nice page layout:
http://www.nkplume.com/
http://www.wzoharbour.com/
http://www.pelvit.com/index.cfm?do=pelvit.home

WEBSITE CLIENT DOES NOT LIKE
http://www.corvanhall.com/
http://www.amberlode-hall.com/
http://www.thesupperfold.co.uk/aboutUs.html
http://www.grainandkettle.com/
http://www.tessmarrow.co.uk/default.asp
http://www.pinnock-halden.co.uk/start.htm
http://www.rilby.co.uk/
http://www.vmkettles.com/default2.aspx
http://www.tumbril-vale.co.uk/mainpage.aspx

COMPANY LOGO
Customer has a company logo (Supplied)

COLOURS:
Blue
White

STRAPLINE:
No

WEBSITE THEME: Marketing

IMAGES THAT BEST REFLECT THE COMPANY:
Spirits / Drinks

HEADER IMAGE:
Spirits / Brands

PAGES:
home
strength& flavour
a little about us
our spirit marketing
big brand success
speak to us

USER JOURNEYS:
General Service > Land on website >Navigation > Info Pages > Contact Form
Questions > Land on website > Message Banners > Info Pages > Contact Form
Contact > Land on website > Clear Telephone / Email Banner > Contact Form

CALL TO ACTION BANNER:
If you need help making your drink the next big brand, speak to us today.

KEYWORDS THAT RELATE TO THE BUSINESS:
brand marketing
drinks marketing
spirits marketing
brand marketing strategy
alcoholic drinks marketing
Drinks Brand Development

LOCATION(S):
United Kingdom -
Worldwide -

Target Market(s)

Male & Female
30-60
Marketing Directors
Brand Developers
Export Directors
Brand Managers

Industry/Entity Type

Marketing

Number of Pages Required

2 pages

Requirements
Must have
• This design will be integrated into wordpress, I have attached a wireframe of what we need, this is NOT a strict guide but contains content that is essential, the wireframes shows the priority of statements and products. the images supplied need to sell the products and services.
The main banner will eventually be animated so this needs to be taken into account.
The cliemt has supplied images which will need to be used in the design , however if you feel you have better images in the same style then they can be used.
Nice to have
• animation included, Jquery
Should not have
• NO fully flash sites or designs, this site will be Search engine optimised and updateable

```html
<!DOCTYPE html>
<html lang="en">
<head>
<meta charset="utf-8">
<title>Tallow &amp; Rye — Drinks Brand Marketing</title>
<link rel="stylesheet" href="https://fonts.googleapis.com/css2?family=Arimo:wght@400;700&family=Gelasio:ital@0;1&display=swap">
<style>
:root{
  --ink-navy:#0d4a63;
  --nav-top:#0f5a73;
  --nav-bottom:#0a3f55;
  --hero-light:#2bb4d6;
  --hero-mid:#1596c4;
  --hero-dark:#0c6f9b;
  --white:#ffffff;
  --band-grey:#cccccc;
  --ribbon:#1883a8;
  --ribbon-dark:#0b4e68;
  --body-teal:#0b4a66;
  --footer-grey:#6b6b6b;
  --cta-top:#ffffff;
  --cta-bottom:#d7d7d7;
  --photo-warm:#5a3020;
  --photo-deep:#1c1420;
}
*{box-sizing:border-box;margin:0;padding:0}
html,body{width:1200px;height:1151px;overflow:hidden;background:var(--white)}
body{font-family:"Arimo",Arial,sans-serif;position:relative;color:var(--ink-navy)}
a{text-decoration:none}

.site-header{position:absolute;left:0;top:0;width:1200px;height:77px;background:var(--white)}
.brand-badge{position:absolute;left:492px;top:-68px;width:216px;height:216px;border-radius:50%;background:var(--white);z-index:3;box-shadow:0 4px 8px rgba(0,0,0,.15)}
.brand-name{position:absolute;left:0;top:30px;width:1200px;text-align:center;font-weight:700;font-size:19px;letter-spacing:.5px;color:#111;z-index:4}
.contact{position:absolute;right:40px;top:10px;text-align:right;z-index:4}
.contact-phone{font-size:30px;font-weight:700;color:var(--ink-navy);display:flex;align-items:center;justify-content:flex-end;gap:6px}
.contact-email{font-size:15px;color:var(--ink-navy);display:flex;align-items:center;justify-content:flex-end;gap:7px;margin-top:4px}

.main-nav{position:absolute;left:0;top:77px;width:1200px;height:79px;background:linear-gradient(var(--nav-top),var(--nav-bottom));z-index:2}
.nav-item{position:absolute;top:0;height:79px;color:var(--white);display:flex;flex-direction:column;justify-content:center}
.nav-item small{font-size:17px;opacity:.95;line-height:1.1}
.nav-item span{font-size:22px;line-height:1.2}
.nav-rule{position:absolute;top:4px;height:70px;border-left:1px dotted rgba(255,255,255,.55)}

.hero{position:absolute;left:0;top:156px;width:1200px;height:575px;background:radial-gradient(ellipse at 20% 10%,var(--hero-light),var(--hero-mid) 45%,var(--hero-dark) 100%)}
.hero-photo{position:absolute;left:91px;top:47px;width:570px;height:480px;background:var(--white);padding:10px;box-shadow:0 3px 10px rgba(0,0,0,.35)}
.hero-photo div{width:100%;height:100%;background:radial-gradient(ellipse at 55% 45%,#c9b08a 0%,var(--photo-warm) 40%,var(--photo-deep) 85%)}
.slide-arrow{position:absolute;top:209px;width:38px;height:38px;border-radius:50%;background:var(--ink-navy);box-shadow:0 2px 4px rgba(0,0,0,.3)}
.slide-arrow svg{display:block}
.testimonial{position:absolute;left:676px;top:80px;width:442px;color:var(--white);font-family:"Gelasio",Georgia,serif}
.testimonial blockquote{font-style:italic;font-size:44px;line-height:57px;text-shadow:0 2px 4px rgba(0,0,0,.3);padding-left:42px;position:relative;white-space:nowrap}
.testimonial blockquote::before{content:"\201C";position:absolute;left:0;top:-4px;font-size:54px}
.testimonial blockquote::after{content:"\201D";font-size:54px;line-height:0;vertical-align:-6px;margin-left:6px}
.testimonial cite{display:block;text-align:right;font-style:normal;font-size:27px;line-height:34px;margin-top:22px;padding-right:2px;text-shadow:0 1px 3px rgba(0,0,0,.3)}
.testimonial cite b{display:block;font-family:"Arimo",Arial,sans-serif;font-weight:400;font-size:26px}
.cta{position:absolute;left:721px;top:391px;width:395px;height:136px;border-radius:5px;background:linear-gradient(var(--cta-top),var(--cta-bottom));box-shadow:0 3px 8px rgba(0,0,0,.3);text-align:center;color:#444}
.cta p{font-size:18px;line-height:22px;margin-top:22px}
.cta strong{display:flex;justify-content:center;align-items:center;gap:12px;font-weight:400;font-size:36px;color:var(--ink-navy);margin-top:12px}

.features{position:absolute;left:0;top:731px;width:1200px;height:323px;background:var(--band-grey)}
.feature{position:absolute;top:32px;width:348px;height:254px;background:var(--white);border-radius:4px;box-shadow:0 2px 5px rgba(0,0,0,.15)}
.feature-ribbon{position:absolute;left:-18px;top:12px;width:384px;height:57px;background:linear-gradient(var(--ribbon),var(--ribbon-dark));color:var(--white);font-size:19px;font-weight:400;line-height:57px;padding-left:30px;white-space:nowrap;letter-spacing:-.2px}
.feature-ribbon::before,.feature-ribbon::after{content:"";position:absolute;top:-8px;border-bottom:8px solid #07394d}
.feature-ribbon::before{left:0;border-left:18px solid transparent}
.feature-ribbon::after{right:0;border-right:18px solid transparent}
.feature p{position:absolute;left:23px;top:92px;width:310px;font-size:15.5px;line-height:20px;color:var(--body-teal)}
.read-more{position:absolute;right:22px;top:216px;font-size:16.5px;color:var(--body-teal);display:flex;align-items:center;gap:6px}

.site-footer{position:absolute;left:0;top:1054px;width:1200px;height:97px;background:var(--white)}
.footer-links{position:absolute;left:115px;top:34px;font-size:13px;line-height:18px;color:var(--footer-grey)}
.social{position:absolute;top:28px;display:flex;align-items:center;gap:6px;font-size:13px;color:var(--ink-navy)}
.social i{display:block;width:14px;height:14px;background:var(--hero-mid)}
</style>
</head>
<body>

<header class="site-header">
  <div class="brand-badge"></div>
  <div class="brand-name">TALLOW &amp; RYE</div>
  <div class="contact">
    <div class="contact-phone">
      <svg width="28" height="28" viewBox="0 0 28 28" aria-hidden="true"><path d="M6 4c-3 2-3 6 0 11s7 9 11 10c3 1 5-1 6-3l-4-4-3 2c-3-1-6-5-7-8l2-3-4-5z" fill="#222"/></svg>
      020 7946 0123
    </div>
    <div class="contact-email">
      <svg width="16" height="13" viewBox="0 0 16 13" aria-hidden="true"><rect x="0.5" y="0.5" width="15" height="12" rx="2" fill="#fff" stroke="#1883a8"/><path d="M1 2l7 5 7-5" fill="none" stroke="#1883a8"/></svg>
      info@tallowandrye.com
    </div>
  </div>
</header>

<nav class="main-nav">
  <a class="nav-item" style="left:58px"><span>Home</span></a>
  <i class="nav-rule" style="left:141px"></i>
  <a class="nav-item" style="left:179px"><small>Tallow</small><span>&amp; Rye</span></a>
  <i class="nav-rule" style="left:309px"></i>
  <a class="nav-item" style="left:343px"><small>A Little Bit</small><span>About Us</span></a>
  <i class="nav-rule" style="left:461px"></i>
  <i class="nav-rule" style="left:741px"></i>
  <a class="nav-item" style="left:774px"><small>Our Spirit</small><span>Marketing</span></a>
  <i class="nav-rule" style="left:906px"></i>
  <a class="nav-item" style="left:944px"><small>Big Brand</small><span>Success</span></a>
  <i class="nav-rule" style="left:1061px"></i>
  <a class="nav-item" style="left:1097px"><small>Speak</small><span>To Us</span></a>
</nav>

<section class="hero">
  <div class="hero-photo"><div role="img" aria-label="Cocktail glass with a physalis garnish on a dimly lit bar counter"></div></div>
  <a class="slide-arrow" style="left:21px" aria-label="Previous slide"><svg width="38" height="38" viewBox="0 0 38 38"><path d="M22 12l-8 7 8 7" fill="none" stroke="#fff" stroke-width="3.5"/></svg></a>
  <a class="slide-arrow" style="left:1140px" aria-label="Next slide"><svg width="38" height="38" viewBox="0 0 38 38"><path d="M16 12l8 7-8 7" fill="none" stroke="#fff" stroke-width="3.5"/></svg></a>
  <figure class="testimonial">
    <blockquote>Turning our small<br>time whisky into a<br>national brand</blockquote>
    <cite>Daniel Hesketh<b>Corvessa</b></cite>
  </figure>
  <a class="cta">
    <p>If you need help<br>making your drink the next big brand,</p>
    <strong>Speak to Us Today <svg width="20" height="34" viewBox="0 0 20 34" aria-hidden="true"><path d="M2 2l16 15L2 32z" fill="#0d4a63"/></svg></strong>
  </a>
</section>

<section class="features">
  <article class="feature" style="left:25px">
    <h2 class="feature-ribbon">22 years experience with big brands</h2>
    <p>Lorem ipsum dolor sit amet, consectetur adipiscing elit. Morbi semper tincidunt enim, in eleifend augue egestas ut. Aliquam ornare ipsum in erat rutrum non venenatis rutrum rutrum sodales.</p>
    <a class="read-more">Read More <svg width="20" height="20" viewBox="0 0 20 20" aria-hidden="true"><circle cx="10" cy="10" r="10" fill="#0d4a63"/><path d="M8 5l5 5-5 5" fill="none" stroke="#fff" stroke-width="2.5"/></svg></a>
  </article>
  <article class="feature" style="left:428px">
    <h2 class="feature-ribbon">Making your drink the next big brand</h2>
    <p>Lorem ipsum dolor sit amet, consectetur adipiscing elit. Morbi semper tincidunt enim, in eleifend augue egestas ut. Aliquam ornare ipsum in erat rutrum non venenatis rutrum rutrum sodales.</p>
    <a class="read-more">Read More <svg width="20" height="20" viewBox="0 0 20 20" aria-hidden="true"><circle cx="10" cy="10" r="10" fill="#0d4a63"/><path d="M8 5l5 5-5 5" fill="none" stroke="#fff" stroke-width="2.5"/></svg></a>
  </article>
  <article class="feature" style="left:828px">
    <h2 class="feature-ribbon">350 outlets that listen to what we say</h2>
    <p>Lorem ipsum dolor sit amet, consectetur adipiscing elit. Morbi semper tincidunt enim, in eleifend augue egestas ut. Aliquam ornare ipsum in erat rutrum non venenatis rutrum rutrum sodales.</p>
    <a class="read-more">Read More <svg width="20" height="20" viewBox="0 0 20 20" aria-hidden="true"><circle cx="10" cy="10" r="10" fill="#0d4a63"/><path d="M8 5l5 5-5 5" fill="none" stroke="#fff" stroke-width="2.5"/></svg></a>
  </article>
</section>

<footer class="site-footer">
  <div class="footer-links">
    brand marketing I brand marketing strategy I drinks marketing I spirits marketing I alcoholic drinks marketing I drinks brand development<br>
    © 1999-2010 Tallow &amp; Rye I terms and conditions I privacy policy
  </div>
  <a class="social" style="left:1000px"><i></i>Chatterly</a>
  <a class="social" style="left:1090px"><i></i>Friendsbook</a>
</footer>

</body>
</html>
```